Postcard Design

We need a postcard design for our company, Calvera Business Group. Our firm sources funding (money) solutions for existing small business owners and start-up who are seeking $50,000 to $250,000. We would like to see designs that feature the colors dark or navy blue and gold. (We are uploading our logo for color reference ONLY. We DO NOT want the logo to be a part of the design!) The final design should communicate that we are an established financial source for business owners who are looking for capital to borrow. The final design should also emphasize that we provide quick approval and fast turnaround.
Target Market(s)
Small business owners (less than 10 employees) as well as start-up companies.
Industry/Entity Type
Small Business

```html
<!DOCTYPE html>
<html lang="en">
<head>
<meta charset="utf-8">
<title>Calvera Business Group – Funding Postcard</title>
<link rel="stylesheet" href="https://fonts.googleapis.com/css2?family=PT+Sans+Narrow:wght@400;700&display=swap">
<style>
  :root {
    --navy-deep: #0b1538;
    --navy-band: #1c2a5c;
    --periwinkle: #6171ad;
    --gold: #d8ac2c;
    --white: #ffffff;
    --photo-light: #c9ccd2;
    --photo-mid: #8593a8;
    --photo-dark: #3d4657;
  }
  html, body {
    margin: 0;
    padding: 0;
    overflow: hidden;
    background: #ffffff;
  }
  .postcard {
    position: relative;
    width: 1200px;
    height: 930px;
    overflow: hidden;
    font-family: "PT Sans Narrow", "Arial Narrow", sans-serif;
    color: var(--white);
  }
  .headline-panel {
    position: absolute;
    left: 0;
    top: 0;
    width: 657px;
    height: 565px;
    background: var(--navy-deep);
  }
  .headline {
    position: absolute;
    left: 57px;
    top: 110px;
    margin: 0;
    font-weight: 400;
    font-size: 72px;
    line-height: 88px;
    letter-spacing: -0.5px;
  }
  .offer-panel {
    position: absolute;
    left: 0;
    top: 565px;
    width: 657px;
    height: 365px;
    background: var(--navy-band);
  }
  .amount {
    position: absolute;
    left: 55px;
    top: 60px;
    margin: 0;
    font-weight: 400;
    font-size: 51px;
    letter-spacing: -0.5px;
  }
  .details {
    position: absolute;
    left: 57px;
    top: 152px;
    width: 500px;
    margin: 0;
    font-size: 20.5px;
    line-height: 30px;
    color: var(--periwinkle);
  }
  .photo {
    position: absolute;
    left: 657px;
    top: 0;
    width: 543px;
    height: 930px;
    background: linear-gradient(135deg, var(--photo-light) 0%, var(--photo-mid) 45%, var(--photo-dark) 100%);
  }
  .ribbon {
    position: absolute;
    left: 579px;
    top: 815px;
    width: 621px;
    height: 69px;
  }
  .ribbon svg {
    position: absolute;
    inset: 0;
  }
  .ribbon-text {
    position: absolute;
    left: 88px;
    top: 0;
    margin: 0;
    line-height: 69px;
    font-size: 36px;
    white-space: nowrap;
  }
</style>
</head>
<body>
<div class="postcard">
  <section class="headline-panel">
    <h1 class="headline">Funding Solutions<br>for existing small<br>business owners<br>and start-ups</h1>
  </section>

  <section class="offer-panel">
    <h2 class="amount">From $50,000 to $250,000</h2>
    <p class="details">Lorem ipsum dolor sit amet, consectetur adipiscing elit, sed do eiusmod tempor incididunt ut labore et dolore magna aliqua. Ut enim ad minim veniam, quis nostrud exercitation ullamco laboris nisi ut aliquip ex ea commodo consequat.</p>
  </section>

  <div class="photo" role="img" aria-label="Photo of two business professionals reviewing loan documents with an advisor"></div>

  <div class="ribbon">
    <svg width="621" height="69" viewBox="0 0 621 69" aria-hidden="true">
      <polygon points="0,0 621,0 621,69 0,69 16,34.5" fill="var(--gold)"/>
    </svg>
    <p class="ribbon-text">Quick approval and fast turnaround.</p>
  </div>
</div>
</body>
</html>
```